KLV Messaging - veteran and exclusive boutique copywriting agency

PROJECT NEEDS:
1. Website design - full homepage design and inner page top banner design
2. Logo design
* Please see attached Briefs (Word Docs) for descriptions of what is needed for 1 and 2 above.
ABOUT THE CLIENT:
KLV Messaging is a veteran and exclusive boutique copywriting agency run by Marcus Holloway. Marcus is an award-winning published novelist and an accomplished executive ghostwriter with articles regularly published prominent technology publications like Brisk, ByteHarbor, FoundryPulse, and more. For nearly three decades, Marcus has focused solely on the technology sector - serving clients in Israel, Europe and the US.

Target Market(s)

hi-tech companies run by serious, confident professionals.

Industry/Entity Type

Business

Number of Pages Required

2 page

Font styles to use
Sans Serif
Other font styles liked:
• font should be modern

Colors
0054AA
0677BA
7BADD7
CADEEF
E8F1F8
F0912C
F2A743
F7CA91
FBE8D2
FDF5EE

Requirements
Must have
• psd files for logo, homepage design, and inner page top banner design
Nice to have
• Please see attached Website and Logo Design Briefs (Word Docs)
Should not have

```html
<!DOCTYPE html>
<html lang="en">
<head>
<meta charset="utf-8">
<title>KLV Messaging</title>
<link rel="stylesheet" href="https://fonts.googleapis.com/css2?family=Poppins:wght@400;500;600;700;800&family=Lato:wght@400;700&display=swap">
<style>
:root{
  --blue:#0054AA;
  --blue-mid:#0677BA;
  --blue-deep:#0a3f86;
  --navy:#15233a;
  --orange:#F0912C;
  --orange-soft:#F2A743;
  --ink:#111;
  --grey:#777;
  --footer:#1c1c1c;
  --footer-bar:#111;
  --white:#fff;
}
*{box-sizing:border-box;margin:0;padding:0}
html,body{width:1200px;height:2623px;overflow:hidden}
body{position:relative;font-family:'Lato',sans-serif;color:var(--ink);background:var(--white)}
.abs{position:absolute}
.heading{font-family:'Poppins',sans-serif}

/* hero */
.hero{left:0;top:0;width:1200px;height:501px;background:linear-gradient(100deg,var(--blue) 0%,#0b4592 35%,#1b2c4c 62%,#1f2430 100%);overflow:hidden}
.hero-swirl{left:-160px;top:-120px;width:760px;height:760px;border-radius:50%;border:90px solid rgba(255,255,255,.05)}
.logo{color:var(--white);font-family:'Poppins',sans-serif;text-align:center;line-height:1}
.logo .mark{font-size:34px;font-weight:700;letter-spacing:8px}
.logo .sub{font-size:16px;font-weight:600;margin-top:6px;letter-spacing:.2px}
.nav{left:367px;top:37px;display:flex;gap:32px;font-family:'Poppins',sans-serif;font-size:14.5px;font-weight:500;color:var(--white)}
.nav .active{font-weight:700;border-bottom:2px solid var(--white);padding-bottom:2px}
.btn{background:var(--white);color:var(--blue);font-family:'Poppins',sans-serif;font-weight:600;display:flex;align-items:center;justify-content:center;border-radius:2px;box-shadow:0 4px 10px rgba(0,0,0,.18)}
.hero-kicker{left:111px;top:188px;color:var(--white);font-family:'Poppins',sans-serif;font-weight:600;font-size:15.5px;letter-spacing:4px}
.hero-title{left:109px;top:218px;color:var(--white);font-size:47px;font-weight:700;letter-spacing:.5px}
.hero-copy{left:111px;top:280px;width:420px;color:var(--white);font-size:15.5px;line-height:29px}
.hero-photo{left:700px;top:72px;width:312px;height:430px;border-radius:150px 150px 0 0;background:linear-gradient(180deg,#8f7c72 0%,#8fb0d6 28%,#7ea3cf 70%,#6b8fbe 100%)}
.strip{left:0;top:501px;width:1200px;height:99px;background:var(--blue-deep);display:flex;align-items:center;justify-content:space-between;padding:0 110px}
.client{display:flex;align-items:center;gap:8px;color:var(--white);font-family:'Poppins',sans-serif;font-size:15px;font-weight:500}
.client .dot{width:24px;height:24px;border-radius:50%;border:2px solid var(--white)}

/* services */
.sec-title{width:1200px;left:0;text-align:center;font-family:'Poppins',sans-serif;font-size:38px;font-weight:500;color:var(--ink)}
.sec-title b{color:var(--orange);font-weight:700}
.card{width:298px;height:389px;top:717px;background:var(--white);box-shadow:0 4px 18px rgba(0,0,0,.08);border-radius:3px}
.card.featured{border:2px solid var(--orange);border-radius:6px}
.card-img{position:absolute;left:0;top:0;width:100%;height:235px}
.card-body{position:absolute;left:11px;right:11px;top:196px;bottom:8px;background:var(--white);border-radius:4px 4px 0 0;text-align:center;padding-top:16px}
.card-body h3{font-family:'Poppins',sans-serif;font-weight:500;font-size:21px;color:var(--ink)}
.card-body p{font-size:14.5px;line-height:25px;color:var(--grey);margin:6px 14px 0}
.card.featured h3{color:var(--orange);font-weight:600}
.card.featured p{color:var(--ink);margin:6px 8px 0}
.more{display:inline-block;margin-top:5px;font-family:'Poppins',sans-serif;font-weight:500;font-size:15px;color:var(--ink);border-bottom:1px solid currentColor;line-height:18px}
.card.featured .more{color:var(--orange)}

/* why */
.why{left:0;top:1206px;width:1200px;height:455px;background:linear-gradient(90deg,#ee9133 0%,#f29b3f 60%,#f0a24b 100%)}
.why-photo{left:108px;top:1160px;width:392px;height:501px;border-radius:180px 180px 0 0;background:linear-gradient(180deg,#9a8376 0%,#91b1d8 25%,#7fa3cf 100%)}
.why-title{left:583px;top:1270px;color:var(--white);font-size:38px;font-weight:500}
.why-title b{font-weight:700}
.why-copy{left:586px;top:1325px;width:490px;color:var(--white);font-size:15px;line-height:29.3px}
.why-copy p+p{margin-top:29px}

/* testimonials */
.quote{width:312px;background:#f5f6f8;border:1px solid #dcdcdc;padding:22px 24px 0 16px}
.quote.raised{border:none;box-shadow:0 4px 20px rgba(0,0,0,.06)}
.stars{color:var(--orange-soft);font-size:20px;letter-spacing:1px;padding-left:4px}
.quote p{font-family:'Poppins',sans-serif;font-size:16px;line-height:27.5px;color:#222;margin-top:12px}
.who{display:flex;align-items:center;gap:12px;margin-top:20px}
.avatar{width:64px;height:64px;border-radius:50%;background:linear-gradient(180deg,#c9a58b,#6f7b86)}
.who .name{font-family:'Poppins',sans-serif;font-weight:700;font-size:16px}
.who .place{font-family:'Poppins',sans-serif;font-size:14px;color:#999;margin-top:3px}

/* footer */
.footer{left:0;top:2220px;width:1200px;height:340px;background:var(--footer);color:var(--white)}
.footer-bar{left:0;top:2560px;width:1200px;height:63px;background:var(--footer-bar);color:var(--white);font-family:'Poppins',sans-serif;font-size:15px;text-align:center;line-height:63px}
.f-head{font-family:'Poppins',sans-serif;font-size:20px;font-weight:600}
.f-list{list-style:none;margin-top:16px}
.f-list li{display:flex;align-items:center;gap:10px;font-size:15.5px;height:34.3px}
.social{display:flex;gap:22px}
.social span{width:31px;height:31px;border-radius:50%;background:var(--white)}
.contact{display:flex;gap:12px;font-size:15.5px;line-height:27px}
.c-ico{width:32px;height:32px;border-radius:50%;background:var(--white);display:flex;align-items:center;justify-content:center;flex:none}
</style>
</head>
<body>

<section class="hero abs" aria-label="Introduction">
  <div class="hero-swirl abs"></div>
  <div class="hero-photo abs" role="img" aria-label="Portrait of the copywriter in a light blue shirt"></div>
</section>

<div class="logo abs" style="left:110px;top:20px;width:164px">
  <div class="mark">KLV</div>
  <div class="sub">MESSAGING</div>
</div>
<nav class="nav abs">
  <span class="active">HOME</span><span>ABOUT</span><span>SERVICES</span><span>INDUSTRIES</span><span>PORTFOLIO</span><span>CLIENTS</span>
</nav>
<div class="btn abs" style="left:964px;top:27px;width:125px;height:43px;font-size:14px">CONTACT US</div>

<div class="hero-kicker abs">WELCOME TO KLV MESSAGING</div>
<h1 class="hero-title heading abs">YOUR VOICE, MY WORDS</h1>
<p class="hero-copy abs">Copywriting and executive ghostwriting that speaks for your vision and your technology.</p>
<div class="btn abs" style="left:110px;top:355px;width:149px;height:51px;font-size:16px">GET STARTED</div>

<div class="strip abs" aria-label="Clients">
  <div class="client"><span class="dot"></span>Linkwell</div>
  <div class="client"><span class="dot"></span>Novaline</div>
  <div class="client"><span class="dot"></span>Arcspring</div>
  <div class="client" style="font-size:24px">Tallmere</div>
  <div class="client"><span class="dot"></span>Linkwell</div>
  <div class="client"><span class="dot"></span>Novaline</div>
  <div class="client"><span class="dot"></span>Summitry</div>
</div>

<h2 class="sec-title abs" style="top:652px">WHAT <b>I DO</b></h2>

<article class="card abs" style="left:111px">
  <div class="card-img" role="img" aria-label="Woman reading messages on her phone by a window" style="background:linear-gradient(120deg,#d9d9d9,#7d7d7d 60%,#2a2a2a)"></div>
  <div class="card-body">
    <h3>Messaging</h3>
    <p>Sometimes, it's good to step back, take a breath, and refresh your perspective. Sometimes, a fresh view of your market and messages</p>
    <span class="more">Read More</span>
  </div>
</article>
<article class="card featured abs" style="left:451px">
  <div class="card-img" role="img" aria-label="Hands typing on a laptop with floating digital icons" style="background:linear-gradient(135deg,#3d5a80,#98aac4 55%,#dde3ec);border-radius:4px 4px 0 0"></div>
  <div class="card-body">
    <h3>Collateral &amp; Creative</h3>
    <p>From company and product names, through taglines and slogans, to web content, data sheets, brochures and more - KLV Messaging</p>
    <span class="more">Read More</span>
  </div>
</article>
<article class="card abs" style="left:791px">
  <div class="card-img" role="img" aria-label="Woman presenting to colleagues in an office" style="background:linear-gradient(120deg,#b9c3c9,#8d9aa3 50%,#d88a45 75%,#c8d0d4)"></div>
  <div class="card-body">
    <h3>Content Marketing</h3>
    <p>At KLV Messaging, we excel at creating marketable content that's in-line with the excellence of your offering.</p>
    <span class="more">Read More</span>
  </div>
</article>

<section class="why abs" aria-label="Why choose me"></section>
<div class="why-photo abs" role="img" aria-label="Portrait of the copywriter smiling"></div>
<h2 class="why-title heading abs">WHY <b>CHOOSE ME</b></h2>
<div class="why-copy abs">
  <p>My writing is concise, elegant, and professional - while at the same time reflecting an understated creativity and sense of humor that brings company messages to a very intimate, personal level.</p>
  <p>I offer clients a deep understanding of business, communication, and technology - coupled with a hard-hitting and concise, yet elegant writing style.</p>
</div>
<div class="btn abs" style="left:586px;top:1546px;width:149px;height:51px;font-size:16px;font-weight:500">READ MORE</div>

<h2 class="sec-title abs" style="top:1707px">WHAT <b>THEY’RE SAYING</b></h2>

<div class="quote abs" style="left:111px;top:1780px;height:341px">
  <div class="stars">★★★★★</div>
  <p>Temporibus autem quibusdam et aut officiis debitis aut rerum neus saepe facere mus, onis voluptas eveniet ut et voluptates repudae sint et molestiae non lorem recusadae.</p>
  <div class="who"><div class="avatar" role="img" aria-label="Photo of Graham Ellis"></div><div><div class="name">Graham Ellis</div><div class="place">United States</div></div></div>
</div>
<div class="quote raised abs" style="left:453px;top:1819px;height:341px">
  <div class="stars">★★★★★</div>
  <p>Itaque earum rerum hic tenetur<br>a sapiene delectus, ut aut reicieis volupatibus maiores alias conse uatur aut perferndis doloribus asperiores reiciendis voluptatbus repellat</p>
  <div class="who" style="margin-top:12px"><div class="avatar" role="img" aria-label="Photo of Lianne" style="border:2px solid var(--orange)"></div><div><div class="name">Lianne</div><div class="place">United States</div></div></div>
</div>
<div class="quote abs" style="left:793px;top:1780px;height:341px">
  <div class="stars">★★★★★</div>
  <p>At vero eos et accusamus et<br>iusto odio dignissimos ducimus qui blaiis praesentium volupttum deleniti atque corrupti quos dolores et quas occaecati cupie non provident</p>
  <div class="who"><div class="avatar" role="img" aria-label="Photo of Owen Marsh"></div><div><div class="name">Owen Marsh</div><div class="place">United States</div></div></div>
</div>
<div class="quote abs" style="left:1141px;top:1823px;height:341px">
  <div class="stars">★★★★★</div>
  <p>At vero eos et accusamus et<br>iusto odio dignissimos ducimus qui blaiis praesentium volupttum deleniti atque corrupti quos dolores et quas occaecati cupie non provident</p>
  <div class="who"><div class="avatar" role="img" aria-label="Photo of a client"></div><div><div class="name">Client</div><div class="place">United States</div></div></div>
</div>

<footer class="footer abs">
  <div class="logo abs" style="left:110px;top:76px;width:164px">
    <div class="mark">KLV</div>
    <div class="sub">MESSAGING</div>
  </div>
  <div class="social abs" style="left:111px;top:154px" aria-label="Social profiles"><span></span><span></span><span></span><span></span></div>

  <div class="abs" style="left:430px;top:75px">
    <div class="f-head">QUICK LINKS</div>
    <ul class="f-list">
      <li><svg width="13" height="13" viewBox="0 0 13 13"><path d="M1 6.5h10M6.5 2l4.5 4.5L6.5 11" stroke="#fff" stroke-width="2.4" fill="none"/></svg>Home</li>
      <li><svg width="13" height="13" viewBox="0 0 13 13"><path d="M1 6.5h10M6.5 2l4.5 4.5L6.5 11" stroke="#fff" stroke-width="2.4" fill="none"/></svg>About</li>
      <li><svg width="13" height="13" viewBox="0 0 13 13"><path d="M1 6.5h10M6.5 2l4.5 4.5L6.5 11" stroke="#fff" stroke-width="2.4" fill="none"/></svg>Services</li>
      <li><svg width="13" height="13" viewBox="0 0 13 13"><path d="M1 6.5h10M6.5 2l4.5 4.5L6.5 11" stroke="#fff" stroke-width="2.4" fill="none"/></svg>Industries</li>
      <li><svg width="13" height="13" viewBox="0 0 13 13"><path d="M1 6.5h10M6.5 2l4.5 4.5L6.5 11" stroke="#fff" stroke-width="2.4" fill="none"/></svg>Contact Us</li>
    </ul>
  </div>
  <div class="abs" style="left:662px;top:75px">
    <div class="f-head">HELP LINKS</div>
    <ul class="f-list">
      <li><svg width="13" height="13" viewBox="0 0 13 13"><path d="M1 6.5h10M6.5 2l4.5 4.5L6.5 11" stroke="#fff" stroke-width="2.4" fill="none"/></svg>FAQ</li>
      <li><svg width="13" height="13" viewBox="0 0 13 13"><path d="M1 6.5h10M6.5 2l4.5 4.5L6.5 11" stroke="#fff" stroke-width="2.4" fill="none"/></svg>Terms of use</li>
      <li><svg width="13" height="13" viewBox="0 0 13 13"><path d="M1 6.5h10M6.5 2l4.5 4.5L6.5 11" stroke="#fff" stroke-width="2.4" fill="none"/></svg>Privacy Policy</li>
      <li><svg width="13" height="13" viewBox="0 0 13 13"><path d="M1 6.5h10M6.5 2l4.5 4.5L6.5 11" stroke="#fff" stroke-width="2.4" fill="none"/></svg>Support Links</li>
      <li><svg width="13" height="13" viewBox="0 0 13 13"><path d="M1 6.5h10M6.5 2l4.5 4.5L6.5 11" stroke="#fff" stroke-width="2.4" fill="none"/></svg>Conditions</li>
    </ul>
  </div>
  <div class="abs" style="left:915px;top:75px">
    <div class="f-head">CONTACT US</div>
    <div class="contact" style="margin-top:18px">
      <span class="c-ico"><svg width="14" height="18" viewBox="0 0 14 18"><path d="M7 0a7 7 0 0 0-7 7c0 5 7 11 7 11s7-6 7-11a7 7 0 0 0-7-7zm0 9.5A2.5 2.5 0 1 1 7 4.5a2.5 2.5 0 0 1 0 5z" fill="#1c1c1c"/></svg></span>
      <span>P.O. Box 1827<br>Ramot, Israel 40415</span>
    </div>
    <div class="contact" style="margin-top:16px;align-items:center">
      <span class="c-ico"><svg width="16" height="16" viewBox="0 0 16 16"><path d="M3.5 1l3 3-1.8 2a9 9 0 0 0 5.3 5.3l2-1.8 3 3-2 2C6.5 14.5 1.5 9.5 1.5 3z" fill="#1c1c1c"/></svg></span>
      <span>+972-52-618-2290</span>
    </div>
    <div class="contact" style="margin-top:18px;align-items:center">
      <span class="c-ico"><svg width="16" height="12" viewBox="0 0 16 12"><rect width="16" height="12" rx="2" fill="#1c1c1c"/><path d="M1 1.5l7 5 7-5" stroke="#fff" stroke-width="1.4" fill="none"/></svg></span>
      <span>hello@klvmsg.co.il</span>
    </div>
  </div>
</footer>
<div class="footer-bar abs">Copyrights@2023.KLV Messaging .All Rights Reserved</div>

</body>
</html>
```